Book Cover design Paws & Petals Book Cover

Please see attached brief Book title BRAVE BESIDE TAILS AND TIDES
THE QUIET GIFT OF CANINES IN LIVING AND HEALING (INCLUSIVE OF THERAPY, EDUCATION, PARENTING, CARE) I have attached a word document describing the brief. Essentially book cover should include a dog and a person, perhaps an older person and a child, and a dog, emotionally charged faces, no cartoons, happy with designer to play with concept and ideas, please avoid AI looking images.

Target Market(s)

Parents, therapists, teachers, people who work with patients/vulnerable people

Industry/Entity Type

Therapeutic care, education, non fiction

Font styles to use
Sans Serif

Requirements
Must have
• Warmth, emotion. I have included the Author photo and paragraph for the back, and also the spec in the details.

```html
<!DOCTYPE html>
<html lang="en">
<head>
<meta charset="utf-8">
<title>Brave Beside Tails and Tides – Book Cover</title>
<link rel="stylesheet" href="https://fonts.googleapis.com/css2?family=Bebas+Neue&family=Arimo:ital,wght@1,700&display=swap">
<style>
  :root {
    --ink-dark: #0b0b09;
    --dusk-blue: #3f5a66;
    --sun-gold: #f3c46a;
    --meadow-brown: #4a3520;
    --title-white: #ffffff;
    --title-yellow: #ffe11a;
    --rule-yellow: #ffe600;
    --portrait-bg: #ffffff;
  }
  * { margin: 0; padding: 0; box-sizing: border-box; }
  html, body { width: 1200px; height: 857px; overflow: hidden; background: var(--ink-dark); }
  .cover {
    position: relative;
    width: 1200px;
    height: 857px;
    overflow: hidden;
    color: var(--title-white);
  }
  .scene {
    position: absolute;
    inset: 0;
    background:
      radial-gradient(ellipse 300px 220px at 930px 130px, rgba(255,214,120,0.85), rgba(243,196,106,0.0) 70%),
      radial-gradient(ellipse 420px 360px at 900px 300px, rgba(150,110,55,0.7), rgba(74,53,32,0) 75%),
      linear-gradient(180deg, var(--dusk-blue) 0%, #2a3a3c 18%, #2b2a1c 40%, #15130d 70%, var(--ink-dark) 100%);
  }
  .scene::after {
    content: "";
    position: absolute;
    inset: 0;
    background: linear-gradient(90deg, rgba(8,8,6,0.55) 0%, rgba(8,8,6,0.25) 45%, rgba(0,0,0,0) 70%);
  }

  /* Back cover */
  .back-blurb {
    position: absolute;
    left: 102px;
    top: 108px;
    width: 380px;
    font-family: "Arimo", Arial, sans-serif;
    font-style: italic;
    font-weight: 700;
    font-size: 15.2px;
    line-height: 20.1px;
    text-shadow: 0 1px 3px rgba(0,0,0,0.6);
  }
  .back-rule {
    position: absolute;
    left: 142px;
    top: 358px;
    width: 292px;
    height: 5px;
    background: var(--rule-yellow);
  }
  .author-portrait {
    position: absolute;
    left: 214px;
    top: 372px;
    width: 151px;
    height: 188px;
    background: linear-gradient(180deg, var(--portrait-bg) 0%, var(--portrait-bg) 40%, #d7b48a 41%, #2a2f6a 75%, #242a60 100%);
  }
  .author-bio {
    position: absolute;
    left: 108px;
    top: 567px;
    width: 370px;
    font-family: "Arimo", Arial, sans-serif;
    font-style: italic;
    font-weight: 700;
    font-size: 11.6px;
    line-height: 15.5px;
  }
  .barcode-panel {
    position: absolute;
    left: 359px;
    top: 712px;
    width: 185px;
    height: 110px;
    background: #ffffff;
  }

  /* Spine */
  .spine-text {
    position: absolute;
    font-family: "Bebas Neue", sans-serif;
    color: var(--title-white);
    white-space: nowrap;
    transform-origin: left top;
    transform: rotate(90deg);
  }
  .spine-title { left: 612px; top: 136px; font-size: 27px; letter-spacing: 0.2px; }
  .spine-author { left: 612px; top: 443px; font-size: 27px; }
  .spine-author small { font-size: 15px; }

  /* Front cover */
  .front-title {
    position: absolute;
    left: 720px;
    top: 384px;
    width: 380px;
    text-align: center;
    font-family: "Bebas Neue", sans-serif;
  }
  .title-lead {
    display: block;
    font-size: 156px;
    line-height: 132px;
    color: var(--title-white);
  }
  .title-rest {
    display: block;
    font-size: 86px;
    line-height: 72px;
    color: var(--title-yellow);
  }
  .subtitle {
    display: block;
    margin-top: 6px;
    font-size: 29px;
    line-height: 31px;
    color: var(--title-yellow);
  }
  .front-author {
    position: absolute;
    left: 720px;
    top: 737px;
    width: 380px;
    text-align: center;
    font-family: "Bebas Neue", sans-serif;
    font-size: 50px;
    line-height: 50px;
    color: var(--title-white);
  }
  .front-author small { font-size: 24px; }
</style>
</head>
<body>
<main class="cover">
  <div class="scene" role="img" aria-label="Warm sunset garden photograph: a white farmhouse and meadow flowers, a young child standing beside an older man on a bench stroking a golden retriever"></div>

  <p class="back-blurb">Brave Beside Tails and Tides is a practical and reflective book about the role of dogs in everyday emotional life. It draws on real experience from therapeutic work, education, parenting, and care, showing how dogs offer consistency, comfort and connection during difficult times, and how they in general provide consistent support in growth and learning. It’s written for professionals, parents and carers who live or work alongside dogs in emotionally complex situations and want something honest, useful and grounded in real practice.</p>
  <div class="back-rule"></div>
  <div class="author-portrait" role="img" aria-label="Author portrait photograph on a white background"></div>
  <p class="author-bio">Dr Helena Marsh is the CEO of Meadowlark. She leads national work in therapeutic education, trauma-informed care, and animal-assisted interventions. Helena has over 20 years’ experience across social work, mental health and leadership, and is a parent of three. Her work combines lived experience with professional insight, with a focus on what helps in real life&nbsp; not just in theory.</p>
  <div class="barcode-panel"></div>

  <div class="spine-text spine-title">BRAVE BESIDE TAILS AND TIDES</div>
  <div class="spine-text spine-author"><small>DR</small> HELENA MARSH</div>

  <h1 class="front-title">
    <span class="title-lead">BRAVE</span>
    <span class="title-rest">BESIDE TAILS<br>AND TIDES</span>
    <span class="subtitle">THE QUIET GIFT OF CANINES<br>IN LIVING AND HEALING</span>
  </h1>
  <p class="front-author"><small>DR</small> HELENA MARSH</p>
</main>
</body>
</html>
```